Home and interior page website design for HVAC company - Veltrix Corp.

Create homepage and one interior page website design for an HVAC (Heating and AC) company. Current website is: https://veltrixcorp-example.com/.

Client has specifically asked that the new site look inviting, informative and interactive. They mentioned that the logo on a white background doesn't look appealing and would like to see other options. (I have included the white background one from their current website as well as the one on an image that the client sent me) The site must include their financing widget (we have the code for this) in a prominent place. Image can be found here: https://fundlarkpay-example.com/badges/fundlark-financing.png.

The content from their existing site belongs to the company that built their site and have said we cannot use any of it. This development site (http://veltrixwebd.qmzdev-example.com/) is what we originally created from our template for them before they decided they wanted a custom built site. The content there is what will need to be on the new home page.

We have gathered images from the client that they would like used throughout the site in this folder: https://files.brelvon-example.com/shared/folder/Xk4pQ9wLmZ2rTn7vBc8HyD5sJf3GaE6uWq1NoKi0RtYe?e=7PLWQD. They would like the photos used to be in tune with the topic being spoken about so if the topic is maintenance on a central AC system the photo used to lead that topic should be of a unit being cleaned.

For the testimonials section please also include a button or "Click here for more testimonials" as requested by the client.

Top Level NAV should include: Home, Residential, Commercial, Testimonials, Gallery, About Us, Coupons, Contact Us

For the interior page, we're looking for the same inviting, informative and interactive feel to the site, preferably with a banner of some sort and the form close to the top of the page if not able to keep it above the fold in the banner. Page should also include sections with clients images used to avoid a wall of text.

Example Websites that the client likes:
https://www.corvalheatcoolinc-example.com/
https://www.frostelmg-example.com/?ref=Q8mZt3LpXw2NvB7cRk5YhJ1sDf4GaE9u
https://www.glimtherm-example.com/nny/
https://www.ubrix-example.com/
https://otterclimateny-example.com/

• *Summarized from project description:
-financing image in prominent place
-content from development site
-images from clients folder
-button or "click here.." note in testimonials section
-form above the fold
-logo not on white background

```html
<!DOCTYPE html>
<html lang="en">
<head>
<meta charset="utf-8">
<title>Veltrix Mechanical Contractors — HVAC Services</title>
<link rel="stylesheet" href="https://fonts.googleapis.com/css2?family=Montserrat:wght@400;500;600;700;800&family=Open+Sans:ital,wght@0,400;0,600;0,700;1,400;1,600&family=Bebas+Neue&display=swap">
<style>
:root{
  --red:#e10a0a;
  --navy:#263247;
  --ink:#4a4a4a;
  --heading:#555;
  --grey-bg:#f4f5f9;
  --footer:#262d3b;
  --white:#fff;
}
*{box-sizing:border-box;margin:0;padding:0}
html,body{width:1200px;height:3022px;overflow:hidden}
body{position:relative;font-family:"Open Sans",sans-serif;color:var(--ink);background:var(--white)}
.abs{position:absolute}

/* hero */
.hero{position:absolute;left:0;top:0;width:1200px;height:600px;background:linear-gradient(135deg,#3a3d44 0%,#54575e 45%,#2c2e33 100%)}
.hero-shade{position:absolute;inset:0;background:rgba(0,0,0,.35)}
.brand{position:absolute;left:176px;top:18px;font-family:"Montserrat",sans-serif;font-weight:800;font-size:34px;color:var(--white);letter-spacing:3px;display:flex;align-items:center;gap:10px}
.brand-dot{width:26px;height:26px;border-radius:50%;background:var(--white)}
.topinfo{position:absolute;top:12px;display:flex;gap:12px;align-items:center;color:var(--white);font-family:"Montserrat",sans-serif}
.topinfo small{display:block;font-size:11px}
.topinfo b{display:block;font-size:13px;font-weight:700}
.nav{position:absolute;left:457px;top:55px;display:flex;gap:19px;font-family:"Montserrat",sans-serif;font-size:9.5px;font-weight:700;color:var(--white);text-transform:uppercase}
.hero-title{position:absolute;left:188px;top:196px;width:460px;font-family:"Montserrat",sans-serif;font-weight:800;font-size:46px;line-height:48px;color:var(--white)}
.btn-red{position:absolute;left:188px;top:421px;width:180px;height:36px;background:var(--red);color:var(--white);font-family:"Montserrat",sans-serif;font-weight:700;font-size:12px;display:flex;align-items:center;justify-content:center}
.quote{position:absolute;left:652px;top:168px;width:368px;height:336px;background:#f3f3f3;border-radius:4px;padding:22px 19px}
.quote h2{font-family:"Montserrat",sans-serif;font-weight:800;font-size:26px;color:var(--navy);margin-bottom:14px}
.quote h2 span{color:var(--red)}
.field{height:39px;background:var(--white);margin-bottom:12px;font-size:11px;font-style:italic;color:#777;padding:0 14px;display:flex;align-items:center;text-transform:uppercase}
.btn-navy{width:152px;height:36px;background:var(--navy);color:var(--white);font-family:"Montserrat",sans-serif;font-weight:700;font-size:11px;display:flex;align-items:center;justify-content:center;margin-top:24px}
.emblem{position:absolute;left:570px;width:60px;height:60px;border-radius:50%;background:var(--white);box-shadow:0 2px 8px rgba(0,0,0,.2);display:flex;align-items:center;justify-content:center}
.emblem i{width:40px;height:40px;border-radius:50%;border:3px solid #222}

/* about */
.blk-black{left:167px;top:685px;width:386px;height:408px;background:#000}
.blk-red{left:483px;top:924px;width:133px;height:243px;background:var(--red)}
.photo{position:absolute;background:linear-gradient(160deg,#c8ccd4 0%,#7a8598 45%,#2c3654 100%)}
.about-title{position:absolute;left:658px;top:760px;font-family:"Montserrat",sans-serif;font-weight:700;font-size:34px;line-height:38px;color:var(--heading)}
.about-title span{color:var(--red)}
.rule{position:absolute;height:3px;width:77px;background:var(--red)}
.about-text{position:absolute;left:658px;top:913px;width:362px;font-size:11.5px;line-height:16.8px;color:#555}
.badge{position:absolute;left:658px;top:1032px;width:90px;height:40px;background:#f5a623;border-radius:3px;color:var(--white);font-family:"Open Sans",sans-serif;font-weight:600;font-size:11px;display:flex;align-items:center;justify-content:center}

/* services */
.services{position:absolute;left:0;top:1260px;width:1200px;height:476px;background:var(--grey-bg)}
.sec-title{position:absolute;left:0;width:1200px;text-align:center;font-family:"Montserrat",sans-serif;font-weight:700;font-size:33px;color:var(--heading)}
.sec-text{position:absolute;left:310px;width:580px;text-align:center;font-size:11.5px;line-height:16.8px;color:#555}
.hex{position:absolute;top:1497px;width:108px;height:122px}
.hex-label{position:absolute;top:1647px;width:160px;text-align:center;font-family:"Montserrat",sans-serif;font-weight:600;font-size:12px;line-height:14px;color:#555}

/* blog */
.eyebrow{position:absolute;left:0;top:1801px;width:1200px;text-align:center;font-family:"Montserrat",sans-serif;font-weight:700;font-size:16px;letter-spacing:4px;color:var(--red)}
.card{position:absolute;top:1931px;width:267px;height:296px;background:var(--white);border:1px solid #ddd}
.card-img{height:184px}
.card h3{font-family:"Montserrat",sans-serif;font-weight:500;font-size:13.5px;line-height:16.5px;color:#222;margin:14px 8px 0}
.card .meta{font-size:9px;color:#777;margin:10px 8px 0}
.card .more{font-family:"Montserrat",sans-serif;font-weight:700;font-size:9px;letter-spacing:1.5px;color:var(--red);margin:17px 8px 0}

/* testimonials */
.testi{position:absolute;left:0;top:2332px;width:1200px;height:413px;background:linear-gradient(120deg,#e30a0a 0%,#f02a2a 60%,#d90606 100%)}
.testi-vert{position:absolute;left:112px;top:2570px;transform:rotate(-90deg);transform-origin:left top;font-family:"Montserrat",sans-serif;font-weight:700;font-size:11px;color:var(--white);letter-spacing:.5px}
.qmark{position:absolute;left:173px;top:2462px;font-family:"Bebas Neue",sans-serif;font-size:90px;line-height:90px;color:var(--white)}
.testi-title{position:absolute;left:239px;top:2466px;font-family:"Bebas Neue",sans-serif;font-weight:400;font-size:46px;line-height:43px;color:var(--white);letter-spacing:.5px}
.testi-sub{position:absolute;left:239px;top:2568px;font-family:"Open Sans",sans-serif;font-size:19px;color:var(--white)}
.testi-quote{position:absolute;left:638px;top:2454px;width:390px;font-style:italic;font-size:12px;line-height:16px;color:var(--white)}
.author{position:absolute;left:638px;top:2571px;color:var(--white);font-family:"Montserrat",sans-serif}
.author b{display:block;font-size:14px;font-weight:700}
.author small{display:block;font-size:9px;font-weight:700}
.author em{display:block;font-family:"Open Sans",sans-serif;font-size:10px;font-weight:600;margin-top:2px}
.arrow{position:absolute;top:2584px;width:33px;height:33px;background:var(--white);display:flex;align-items:center;justify-content:center}

/* footer */
.footer{position:absolute;left:0;top:2745px;width:1200px;height:277px;background:var(--footer);color:var(--white)}
.f-head{position:absolute;top:2783px;font-family:"Montserrat",sans-serif;font-weight:700;font-size:14.5px;color:var(--white)}
.f-text{position:absolute;font-size:11px;line-height:19.5px;color:#e7e9ee}
.pay{position:absolute;width:32px;height:19px;border-radius:2px;background:var(--white)}
.f-bottom{position:absolute;left:174px;top:2977px;width:852px;border-top:1px solid #3d4558}
.f-small{position:absolute;top:2995px;font-size:10px;color:#e7e9ee}
</style>
</head>
<body>

<!-- hero -->
<section class="hero" role="img" aria-label="Technicians lifting a rooftop HVAC unit on a city street">
  <div class="hero-shade"></div>
</section>
<div class="brand"><span class="brand-dot"></span>VELTRIX</div>
<div class="topinfo" style="left:736px">
  <svg width="20" height="24" viewBox="0 0 20 24" fill="none" stroke="#fff" stroke-width="2"><path d="M10 22s7-7 7-13a7 7 0 0 0-14 0c0 6 7 13 7 13z"/><circle cx="10" cy="9" r="2.5"/></svg>
  <div><small>Location</small><b>Brooklyn, NY 11299</b></div>
</div>
<div class="topinfo" style="left:908px">
  <svg width="20" height="20" viewBox="0 0 24 24" fill="none" stroke="#fff" stroke-width="2"><path d="M5 3h4l2 5-3 2a12 12 0 0 0 6 6l2-3 5 2v4a2 2 0 0 1-2 2A18 18 0 0 1 3 5a2 2 0 0 1 2-2z"/></svg>
  <div><small>Helpline:</small><b>(718) 555-0147</b></div>
</div>
<nav class="nav"><span>Home</span><span>Residential</span><span>Commercial</span><span>Testimonials</span><span>Gallery</span><span>About Us</span><span>Coupons</span><span>Contact Us</span></nav>
<h1 class="hero-title">Great Costumer Service And Even Better Prices</h1>
<div class="btn-red">CALL US: (718) 555-0147</div>
<form class="quote">
  <h2>GET A <span>FREE QUOTE</span></h2>
  <div class="field">Your Name</div>
  <div class="field">Your Email</div>
  <div class="field">Phone Number</div>
  <div class="field">I'd like a quote for</div>
  <div class="btn-navy">GET A QUOTE</div>
</form>
<div class="emblem" style="top:570px"><i></i></div>

<!-- about -->
<div class="abs blk-black"></div>
<div class="abs blk-red"></div>
<div class="photo" style="left:209px;top:731px;width:386px;height:408px" role="img" aria-label="Technician in hard hat checking gauges on a rooftop AC unit"></div>
<h2 class="about-title">The Ideal Commercial<br>HVAC <span>Service for</span><br>Your Business</h2>
<div class="rule" style="left:658px;top:888px"></div>
<p class="about-text">Whether you want preventative commercial HVAC maintenance for your business center in Brooklyn, NY or a quick repair of your office air conditioner, turn to our technicians. We serve our valued commercial clients with ideal heating and cooling maintenance solutions and invite you to browse our website to find out more about Veltrix Mechanical Contractors.</p>
<div class="badge">FundlarkPay</div>

<!-- services -->
<section class="services"></section>
<div class="emblem" style="top:1244px"><i></i></div>
<h2 class="sec-title" style="top:1320px">Our Services</h2>
<div class="rule" style="left:562px;top:1374px"></div>
<p class="sec-text" style="top:1395px">We offer HVAC repair services that encompass various heating and cooling repairs, from complete outdoor unit repairs to minor interior work. We also do maintenance on a regular basis, keeping every system in proper working order. Learn more on our services page.</p>

<svg class="hex" style="left:257px" viewBox="0 0 108 122"><polygon points="54,1 107,31 107,91 54,121 1,91 1,31" fill="#fff" stroke="#ccc"/><g fill="none" stroke="#e10a0a" stroke-width="2.5"><rect x="34" y="38" width="40" height="44" rx="2"/><path d="M42 48h24M42 56h24M42 64h24M42 72h24"/></g></svg>
<svg class="hex" style="left:456px" viewBox="0 0 108 122"><polygon points="54,1 107,31 107,91 54,121 1,91 1,31" fill="#fff" stroke="#ccc"/><g fill="none" stroke="#e10a0a" stroke-width="2.5"><circle cx="53" cy="60" r="15"/><circle cx="53" cy="60" r="4"/><circle cx="69" cy="76" r="5"/><path d="M40 40c3 4-2 6 1 9"/></g></svg>
<svg class="hex" style="left:645px" viewBox="0 0 108 122"><polygon points="54,1 107,31 107,91 54,121 1,91 1,31" fill="#fff" stroke="#ccc"/><g fill="none" stroke="#e10a0a" stroke-width="2.5"><path d="M42 46l12-10 12 10M47 64v-10M61 64v-10M44 72h20a4 4 0 0 1 0 8H44"/></g></svg>
<svg class="hex" style="left:835px" viewBox="0 0 108 122"><polygon points="54,1 107,31 107,91 54,121 1,91 1,31" fill="#fff" stroke="#ccc"/><g fill="none" stroke="#e10a0a" stroke-width="2.5"><rect x="30" y="42" width="48" height="22" rx="3"/><path d="M36 56h36M40 70c2 4-2 6 0 10M54 70c2 4-2 6 0 10M68 70c2 4-2 6 0 10"/></g></svg>

<div class="hex-label" style="left:231px">Appointments to fit<br>any schedule</div>
<div class="hex-label" style="left:430px">On-site area<br>inspections</div>
<div class="hex-label" style="left:619px">Detailed project<br>assessments</div>
<div class="hex-label" style="left:809px">Honest and upfront<br>estimates</div>

<!-- blog -->
<div class="eyebrow">RECENT RESOURCES</div>
<h2 class="sec-title" style="top:1823px">Read Blog Posts</h2>
<div class="rule" style="left:562px;top:1876px"></div>

<article class="card" style="left:174px">
  <div class="card-img" style="background:linear-gradient(180deg,#2e6fe0 0%,#6b8fc9 55%,#7a4b38 100%)" role="img" aria-label="Technician servicing a heat pump on a rooftop"></div>
  <h3>The Most Common Heat Pump Problems &amp; How To Avoid Them</h3>
  <div class="meta">April 16, 2021 &nbsp;No Comments</div>
  <div class="more">READ MORE</div>
</article>
<article class="card" style="left:466px;box-shadow:0 6px 16px rgba(0,0,0,.12)">
  <div class="card-img" style="background:linear-gradient(135deg,#8b9099 0%,#a9adb3 50%,#e08a2c 100%)" role="img" aria-label="Technician installing a window AC unit"></div>
  <h3>The Optimal HVAC Temperatures To Save The Most On Your Power Bill</h3>
  <div class="meta">April 16, 2021 &nbsp;No Comments</div>
  <div class="more">READ MORE</div>
</article>
<article class="card" style="left:759px">
  <div class="card-img" style="background:linear-gradient(180deg,#d9d6cc 0%,#8c6a4a 50%,#55585c 100%)" role="img" aria-label="Condenser coils being cleaned with foam cleaner"></div>
  <h3>How To Add Home Equity Through HVAC Upgrades</h3>
  <div class="meta">April 16, 2021 &nbsp;No Comments</div>
  <div class="more">READ MORE</div>
</article>

<!-- testimonials -->
<section class="testi" role="img" aria-label="Red-toned background with a smiling family"></section>
<div class="emblem" style="top:2302px"><i></i></div>
<div class="testi-vert">TESTIMONIALS</div>
<div class="qmark">“</div>
<h2 class="testi-title">WHAT OUR CUSTOMERS<br>ARE SAYING</h2>
<div class="testi-sub">VELTRIX MECHANICAL CONTRACTORS</div>
<p class="testi-quote">You provided me with superb assistance with your HVAC maintenance. That helped me out a lot for the upcoming season. The opening event passed perfectly and your service as an HVAC contractor was crucial. I am not one of those people who ignore the role of the many technicians and business partners and take all the credit for themselves only. That's why I give you five stars!</p>
<div class="author"><b>BY MARISOL T. OKAFOR</b><small>ON VELTRIX MECHANICAL CONTRACTORS</small><em>★★★★★<br>Jul 7, 2020</em></div>
<div class="arrow" style="left:956px"><svg width="12" height="14" viewBox="0 0 12 14"><path d="M8 2L3 7l5 5" fill="none" stroke="#111" stroke-width="2"/></svg></div>
<div class="arrow" style="left:994px"><svg width="12" height="14" viewBox="0 0 12 14"><path d="M4 2l5 5-5 5" fill="none" stroke="#111" stroke-width="2"/></svg></div>

<!-- footer -->
<footer class="footer"></footer>
<div class="f-head" style="left:174px">WORKING HOURS</div>
<div class="f-text" style="left:174px;top:2816px">Monday<br>Tuesday<br>Wednesday<br>Thursday<br>Friday<br>Saturday<br>Sunday</div>
<div class="f-text" style="left:313px;top:2816px">8:00am to 5:00pm<br>8:00am to 5:00pm<br>8:00am to 5:00pm<br>8:00am to 5:00pm<br>8:00am to 5:00pm<br>Closed<br>Closed</div>
<div class="f-head" style="left:479px">CONTACT US</div>
<div class="f-text" style="left:479px;top:2810px;line-height:14px;font-size:11.5px">Veltrix Mechanical<br>Contractors</div>
<div class="f-text" style="left:479px;top:2851px">Brooklyn, NY 11299<br>Phone: (718) 555-0147</div>
<div class="f-head" style="left:659px">PAYMENTS ACCEPTED</div>
<div class="pay" style="left:661px;top:2818px"></div>
<div class="pay" style="left:699px;top:2818px"></div>
<div class="pay" style="left:738px;top:2818px"></div>
<div class="pay" style="left:661px;top:2842px"></div>
<div class="pay" style="left:699px;top:2842px"></div>
<div class="pay" style="left:738px;top:2842px"></div>
<div class="f-head" style="left:895px">SERVICES LIST</div>
<div class="f-text" style="left:896px;top:2810px">Heating Repairs<br>AC Repairs<br>Ventilation<br>HVAC Maintenance<br>HVAC Services</div>
<div class="f-bottom"></div>
<div class="f-small" style="left:174px">© Veltrix Mechanical Contractors | 2021. All Rights Reserved.</div>
<div class="f-small" style="left:879px">Terms of Use &nbsp;| &nbsp; Privacy Policy</div>

</body>
</html>
```